Stylish Business Card for Modern hair salon

I need a simple business card design using our salon logo and colours that are in the logo. We service clients of all ages but predominantly those in the 18 to 55 age range. We have a young staff and are looking to have a card that will present a modern and clean image that represents who we are. The card should be in black and white same as our logo. Minimal use of other colours is allowed.

Industry/Entity Type

Hair And Beauty

Contact Information for Business Card

The design should have the following information
salon name - TR Hair Studio
address - 2751 Birchfield Rd.E. Mississauga, ON L7P3K2
phone - 905 614-2870
website - trhairexample.ca
instagram - tr.hairstudio
twitter - @TR_HairStudio

Colors
000000
ffffff
474747

Requirements
Must have
• simple design, salon name, address, phone, website, instagram, twitter info
• Back of card should have the following:
• YOUR NEXT APPOINTMENT
• DATE
• TIME
Nice to have
• simple design, clear to see and read,
• predominantly black and white colour, minimal use of other colours is ok
Should not have
• many colours, various fonts

```html
<!DOCTYPE html>
<html lang="en">
<head>
<meta charset="utf-8">
<title>TR Hair Studio – Business Card</title>
<link rel="stylesheet" href="https://fonts.googleapis.com/css2?family=Oswald:wght@600&family=Roboto:wght@400;700&display=swap">
<style>
  :root {
    --ink: #000000;
    --paper: #ffffff;
    --graphite: #474747;
    --backdrop: #f4f4f4;
  }
  * { margin: 0; padding: 0; box-sizing: border-box; }
  html, body { width: 1200px; height: 1200px; overflow: hidden; }
  body {
    background: var(--backdrop);
    position: relative;
    font-family: "Roboto", Arial, sans-serif;
    color: var(--ink);
  }
  .card {
    position: absolute;
    left: 196px;
    width: 808px;
    height: 462px;
    background: var(--paper);
    overflow: hidden;
  }
  .card--front { top: 80px; }
  .card--back { top: 674px; height: 461px; }

  .card__shapes { position: absolute; inset: 0; }

  .front__name {
    position: absolute;
    left: 38px;
    top: 258px;
    font-family: "Oswald", "Arial Narrow", sans-serif;
    font-weight: 600;
    font-size: 50px;
    line-height: 60px;
    letter-spacing: 1px;
    color: var(--paper);
    text-transform: uppercase;
  }

  .contact { position: absolute; display: flex; align-items: center; }
  .contact__icon { position: absolute; width: 28px; height: 28px; }
  .contact__text { font-size: 17.6px; line-height: 24px; white-space: nowrap; }

  .contact--address { left: 226px; top: 30px; }
  .contact--address .contact__icon { left: 0; top: 0; }
  .contact--address .contact__text { position: absolute; left: 45px; top: 0; }
  .contact--phone { left: 226px; top: 97px; }
  .contact--phone .contact__text { position: absolute; left: 45px; top: 2px; }
  .contact--web { left: 226px; top: 148px; }
  .contact--web .contact__text { position: absolute; left: 47px; top: 2px; }

  .divider {
    position: absolute;
    top: 227px;
    height: 4px;
    width: 192px;
    background: var(--ink);
  }
  .divider--left { left: 270px; }
  .divider--right { left: 594px; }

  .brand-mark {
    position: absolute;
    background: var(--ink);
    color: var(--paper);
    display: flex;
    align-items: center;
    justify-content: center;
    font-family: "Roboto", Arial, sans-serif;
    font-weight: 700;
    letter-spacing: 1px;
    white-space: nowrap;
  }
  .brand-mark--front { left: 482px; top: 190px; width: 93px; height: 77px; font-size: 14px; }
  .brand-mark--back { left: 553px; top: 126px; width: 153px; height: 127px; font-size: 22px; }

  .social { position: absolute; left: 529px; display: flex; align-items: center; }
  .social--instagram { top: 320px; }
  .social--twitter { top: 375px; }
  .social__dot {
    width: 28px; height: 28px;
    border-radius: 50%;
    background: var(--ink);
  }
  .social__handle { margin-left: 23px; font-size: 17.6px; }

  .back__band-top {
    position: absolute; left: 0; top: 0; width: 100%; height: 26px;
    background: var(--ink);
  }
  .back__band-bottom {
    position: absolute; left: 0; top: 370px; width: 100%; height: 91px;
    background: var(--ink);
    display: flex; align-items: center; justify-content: center;
  }
  .back__name {
    font-family: "Oswald", "Arial Narrow", sans-serif;
    font-weight: 600;
    font-size: 50px;
    letter-spacing: 1.5px;
    color: var(--paper);
    text-transform: uppercase;
  }
  .appointment { position: absolute; left: 46px; top: 141px; }
  .appointment__title {
    font-weight: 700;
    font-size: 22.5px;
    letter-spacing: -0.2px;
    margin-bottom: 14px;
  }
  .appointment__field { font-size: 19px; line-height: 39px; }
</style>
</head>
<body>

<section class="card card--front" aria-label="Business card front">
  <svg class="card__shapes" width="808" height="462" viewBox="0 0 808 462" aria-hidden="true">
    <polygon points="0,0 462,462 420,462 0,40" fill="var(--graphite)"/>
    <polygon points="0,40 420,462 0,462" fill="var(--ink)"/>
    <polygon points="596,0 808,0 808,212" fill="var(--graphite)"/>
    <polygon points="630,0 808,0 808,178" fill="var(--ink)"/>
  </svg>

  <h1 class="front__name">TR<br>Hair<br>Studio</h1>

  <div class="contact contact--address">
    <svg class="contact__icon" viewBox="0 0 24 24" aria-hidden="true">
      <path d="M12 1.5a7 7 0 0 0-7 7c0 5.2 7 14 7 14s7-8.8 7-14a7 7 0 0 0-7-7zm0 9.8a2.8 2.8 0 1 1 0-5.6 2.8 2.8 0 0 1 0 5.6z" fill="var(--ink)"/>
    </svg>
    <p class="contact__text">2751 Birchfield Rd.E. Mississauga,<br>ON L7P3K2</p>
  </div>

  <div class="contact contact--phone">
    <svg class="contact__icon" viewBox="0 0 24 24" aria-hidden="true">
      <path d="M6.6 2.2 9.3 6c.4.6.3 1.3-.2 1.8L7.6 9.2c1.3 2.9 3.9 5.6 7 7.1l1.5-1.5c.5-.5 1.2-.6 1.8-.2l3.8 2.6c.6.4.8 1.3.3 1.9l-1.6 2.1c-.6.7-1.5 1-2.4.8C10.1 20 4 13.9 2.1 6.1c-.2-.9.1-1.8.8-2.4L5 2c.5-.5 1.2-.4 1.6.2z" fill="var(--ink)"/>
    </svg>
    <p class="contact__text">905 614-2870</p>
  </div>

  <div class="contact contact--web">
    <svg class="contact__icon" viewBox="0 0 24 24" aria-hidden="true">
      <g fill="none" stroke="var(--ink)" stroke-width="1.2">
        <circle cx="12" cy="12" r="10.5"/>
        <ellipse cx="12" cy="12" rx="4.6" ry="10.5"/>
        <line x1="12" y1="1.5" x2="12" y2="22.5"/>
        <line x1="1.5" y1="12" x2="22.5" y2="12"/>
        <path d="M3 6.5h18M3 17.5h18"/>
      </g>
    </svg>
    <p class="contact__text">trhairexample.ca</p>
  </div>

  <div class="divider divider--left"></div>
  <div class="brand-mark brand-mark--front">TR HAIR</div>
  <div class="divider divider--right"></div>

  <div class="social social--instagram">
    <span class="social__dot" aria-hidden="true"></span>
    <span class="social__handle">tr.hairstudio</span>
  </div>
  <div class="social social--twitter">
    <span class="social__dot" aria-hidden="true"></span>
    <span class="social__handle">@TR_HairStudio</span>
  </div>
</section>

<section class="card card--back" aria-label="Business card back">
  <div class="back__band-top"></div>

  <div class="appointment">
    <h2 class="appointment__title">YOUR NEXT APPOINTMENT</h2>
    <p class="appointment__field">DATE :</p>
    <p class="appointment__field">TIME :</p>
  </div>

  <div class="brand-mark brand-mark--back">TR HAIR</div>

  <div class="back__band-bottom">
    <p class="back__name">TR Hair Studio</p>
  </div>
</section>

</body>
</html>
```